Brightmoor Partners Branding Revamp

We are a consulting company, looking for a way to display and promote our brand. We have 2 sides to the business- Brightmoor (financial) and Partners (cyber security). The financial side products relate to business necessities: card processing, website design/hosting/maintenance, VoIP phone systems. The cyber security side promotes a bundled package of 4 solutions: network vulnerability scan, dark web scan, anti-ransomeware/malware software, and image-level backups. We want people to understand that partnering with Brightmoor Partners gives them “Elevated Peace of Mind” (tagline). Current badge and logos uploaded.

Target Market(s)

Small businesses

Contact Information for Business Card

Lena Marwick, Vice President, lena@brightmoorpartners.example, 555-806-1937, www.brightmoorpartners.example

Requirements
Nice to have
• I do prefer the darker background for front and back

```html
<!DOCTYPE html>
<html lang="en">
<head>
<meta charset="utf-8">
<title>Brightmoor Partners — Business Card</title>
<link rel="stylesheet" href="https://fonts.googleapis.com/css2?family=Michroma&family=Space+Grotesk:wght@300;400;500&display=swap">
<style>
  :root {
    --page: #ffffff;
    --card: #05070c;
    --red: #e3000f;
    --red-deep: #7a0008;
    --white: #f4f4f4;
    --label: #0b0c10;
    --glow: rgba(230, 60, 70, 0.16);
  }
  * { margin: 0; padding: 0; box-sizing: border-box; }
  html, body { width: 1199px; height: 1200px; overflow: hidden; background: var(--page); }
  .sheet { position: relative; width: 1199px; height: 1200px; }

  .side-label {
    position: absolute; left: 0; width: 100%;
    text-align: center;
    font-family: "Michroma", sans-serif;
    font-size: 30px; letter-spacing: 7px;
    color: var(--label);
  }
  .side-label--front { top: 46px; }
  .side-label--back { top: 590px; }

  .card {
    position: absolute; left: 213px; width: 780px; height: 445px;
    background: var(--card);
    overflow: hidden;
    box-shadow: 0 0 80px 30px var(--glow);
  }
  .card--front { top: 106px; }
  .card--back { top: 656px; }

  .front-texture {
    position: absolute; inset: 0;
    background:
      radial-gradient(ellipse 48% 40% at 22% 40%, rgba(140, 10, 20, 0.35), transparent 70%),
      radial-gradient(ellipse 45% 45% at 80% 35%, rgba(150, 10, 20, 0.38), transparent 70%),
      radial-gradient(ellipse 60% 35% at 50% 80%, rgba(110, 5, 15, 0.25), transparent 75%);
  }

  .front-brand {
    position: absolute; left: 0; top: 170px; width: 100%;
    display: flex; flex-direction: column; align-items: center;
  }
  .brand-square {
    width: 54px; height: 54px; background: var(--red);
    margin-bottom: 48px;
  }
  .brand-name {
    font-family: "Michroma", sans-serif;
    color: var(--white);
    text-transform: uppercase;
    text-align: center;
    line-height: 1.35;
  }
  .front-brand .brand-name { font-size: 25px; letter-spacing: 12px; padding-left: 12px; }

  .back-brand {
    position: absolute; left: 56px; top: 52px;
    display: flex; flex-direction: column; align-items: center;
  }
  .back-brand .brand-square { width: 30px; height: 30px; margin-bottom: 14px; }
  .back-brand .brand-name { font-size: 12px; letter-spacing: 5px; padding-left: 5px; }

  .back-texture {
    position: absolute; left: 430px; top: 0; width: 350px; height: 100%;
    background:
      radial-gradient(ellipse 60% 50% at 70% 30%, rgba(200, 10, 25, 0.55), transparent 75%),
      radial-gradient(ellipse 55% 45% at 60% 80%, rgba(210, 10, 25, 0.55), transparent 75%),
      linear-gradient(90deg, transparent 0%, rgba(120, 5, 15, 0.45) 35%, rgba(150, 8, 20, 0.7) 100%);
  }

  .contact {
    position: absolute; left: 54px; top: 238px;
  }
  .contact-name {
    font-family: "Space Grotesk", sans-serif;
    font-weight: 500; font-size: 36px; line-height: 1;
    color: var(--red);
    letter-spacing: 0.2px;
  }
  .contact-title {
    margin-top: 6px;
    font-family: "Michroma", sans-serif;
    font-size: 14px; letter-spacing: 3px;
    color: var(--white);
    font-variant: small-caps;
  }
  .contact-rule {
    width: 276px; height: 1px; margin: 24px 0 10px;
    background: rgba(255, 255, 255, 0.55);
  }
  .contact-list { list-style: none; }
  .contact-list li {
    font-family: "Space Grotesk", sans-serif;
    font-weight: 300; font-size: 15px; line-height: 19.5px;
    color: var(--white);
    letter-spacing: 0.6px;
  }
</style>
</head>
<body>
<main class="sheet">
  <h2 class="side-label side-label--front">FRONT</h2>
  <section class="card card--front">
    <div class="front-texture" role="img" aria-label="Dark red low-poly geometric mesh background"></div>
    <div class="front-brand">
      <div class="brand-square"></div>
      <div class="brand-name">Brightmoor<br>Partners</div>
    </div>
  </section>

  <h2 class="side-label side-label--back">BACK</h2>
  <section class="card card--back">
    <div class="back-texture" role="img" aria-label="Bright red low-poly geometric mesh decoration"></div>
    <div class="back-brand">
      <div class="brand-square"></div>
      <div class="brand-name">Brightmoor<br>Partners</div>
    </div>
    <div class="contact">
      <h1 class="contact-name">Lena Marwick</h1>
      <p class="contact-title">Vice President</p>
      <div class="contact-rule"></div>
      <ul class="contact-list">
        <li>lena@brightmoorpartners.example</li>
        <li>555-806-1937</li>
        <li>www.brightmoorpartners.example</li>
      </ul>
    </div>
  </section>
</main>
</body>
</html>
```